Design some Business Cards & Stationary for KWT

I need a design mockup for a company's business cards and their letterhead. I've attached the logo and listed what company info I want on the cards and letterhead below. Thanks.

Name
Job Title
Address
Office #
Mobile #
Email
Website

```html
<!DOCTYPE html>
<html lang="en">
<head>
<meta charset="utf-8">
<title>KWT Business Cards</title>
<link href="https://fonts.googleapis.com/css2?family=Montserrat:wght@400;600;700&family=Open+Sans:wght@400&display=swap" rel="stylesheet">
<style>
  :root {
    --navy: #1c3b6f;
    --paper: #f4f5f8;
    --white: #ffffff;
    --ink: #4a4d55;
    --backdrop: #e3e5ea;
  }
  html, body {
    margin: 0;
    padding: 0;
    width: 1200px;
    height: 820px;
    overflow: hidden;
    background: var(--backdrop);
  }
  .canvas {
    position: relative;
    width: 1200px;
    height: 820px;
  }
  .card {
    position: absolute;
    width: 560px;
    height: 320px;
    box-shadow: 0 10px 24px rgba(30, 40, 60, 0.18);
    overflow: hidden;
  }
  .card--front {
    left: 70px;
    top: 70px;
    background: var(--navy);
    color: var(--white);
  }
  .card--back {
    left: 570px;
    top: 430px;
    background: var(--paper);
  }
  .wordmark {
    position: absolute;
    left: 0;
    right: 0;
    text-align: center;
    font-family: 'Montserrat', sans-serif;
    font-weight: 700;
    line-height: 1;
  }
  .wordmark__initials { font-size: 104px; letter-spacing: 4px; display: block; }
  .wordmark__name { font-size: 17px; letter-spacing: 6px; display: block; margin-top: 8px; }
  .card--front .wordmark { top: 62px; color: var(--white); }
  .card--front .website {
    position: absolute;
    top: 240px;
    left: 0;
    right: 0;
    text-align: center;
    font-family: 'Open Sans', sans-serif;
    font-size: 13px;
    color: var(--white);
  }
  .back-band {
    position: absolute;
    inset: 0;
  }
  .card--back .wordmark {
    top: 34px;
    left: 40px;
    right: auto;
    width: 300px;
    color: var(--navy);
  }
  .card--back .wordmark__initials { font-size: 74px; }
  .card--back .wordmark__name { font-size: 13px; letter-spacing: 4px; }
  .holder {
    position: absolute;
    right: 22px;
    top: 82px;
    text-align: right;
    font-family: 'Open Sans', sans-serif;
    color: var(--white);
  }
  .holder__name { font-size: 20px; }
  .holder__role { font-size: 12px; }
  .contacts {
    position: absolute;
    left: 26px;
    top: 200px;
    margin: 0;
    padding: 0;
    list-style: none;
    font-family: 'Open Sans', sans-serif;
    font-size: 13px;
    line-height: 17px;
    color: var(--white);
  }
  .contacts li { display: flex; align-items: flex-start; gap: 7px; }
  .contacts svg { width: 11px; height: 11px; margin-top: 3px; flex: none; fill: var(--white); }
</style>
</head>
<body>
<main class="canvas">

  <section class="card card--front" aria-label="Business card front">
    <div class="wordmark">
      <span class="wordmark__initials">KWT</span>
      <span class="wordmark__name">KESTON WORKS TRADE</span>
    </div>
    <div class="website">www.yourwebsite.com</div>
  </section>

  <section class="card card--back" aria-label="Business card back">
    <svg class="back-band" viewBox="0 0 560 320" preserveAspectRatio="none" aria-hidden="true">
      <path d="M0 178 L400 178 L400 80 L430 80 L440 68 L450 80 L560 80 L560 320 L0 320 Z" fill="var(--navy)"/>
    </svg>

    <div class="wordmark">
      <span class="wordmark__initials">KWT</span>
      <span class="wordmark__name">KESTON WORKS TRADE</span>
    </div>

    <div class="holder">
      <div class="holder__name">Mara Quill</div>
      <div class="holder__role">Manage</div>
    </div>

    <ul class="contacts">
      <li>
        <svg viewBox="0 0 12 12"><path d="M6 0a4 4 0 0 0-4 4c0 3 4 8 4 8s4-5 4-8a4 4 0 0 0-4-4zm0 5.5A1.5 1.5 0 1 1 6 2.5a1.5 1.5 0 0 1 0 3z"/></svg>
        <span>your home, your city,<br>your country, box 88900</span>
      </li>
      <li>
        <svg viewBox="0 0 12 12"><path d="M2.5 0.5l2 2.2-1 1.4c.7 1.6 1.8 2.7 3.4 3.4l1.4-1 2.2 2-1 2C5 10.5 1.5 7 0.5 1.5z"/></svg>
        <span>111-222-333</span>
      </li>
      <li>
        <svg viewBox="0 0 12 12"><path d="M3 0h6v12H3zM4 1.5v8h4v-8zM5.5 10.3h1v1h-1z"/></svg>
        <span>111-222-333</span>
      </li>
      <li>
        <svg viewBox="0 0 12 12"><path d="M0 2h12v8H0zM1 3l5 3.5L11 3v-.2H1z"/></svg>
        <span>info@youremail.com</span>
      </li>
      <li>
        <svg viewBox="0 0 12 12"><path d="M6 0a6 6 0 1 0 0 12A6 6 0 0 0 6 0zm0 1.2c.8.8 1.3 2.3 1.4 4.2H4.6C4.7 3.5 5.2 2 6 1.2zM4.6 6.6h2.8c-.1 1.9-.6 3.4-1.4 4.2-.8-.8-1.3-2.3-1.4-4.2z"/></svg>
        <span>www.yourwebsite.com</span>
      </li>
    </ul>
  </section>

</main>
</body>
</html>
```